Checkout sign

Wall sign for clinic checkout.
“The Good Lord does ALL the healing..
But we DO collect the co-pay”

Add Celtic cross at top and our logo on bottom

```html
<!DOCTYPE html>
<html lang="en">
<head>
<meta charset="utf-8">
<title>Harlow Orthopedic Clinic – Checkout Sign</title>
<link rel="stylesheet" href="https://fonts.googleapis.com/css2?family=Oswald:wght@600&family=Archivo:wght@700&display=swap">
<style>
  :root {
    --ink: #21109a;
    --paper: #fafafa;
  }
  html, body {
    margin: 0;
    padding: 0;
    width: 1200px;
    height: 672px;
    overflow: hidden;
    background: var(--paper);
  }
  .sign {
    position: relative;
    width: 1200px;
    height: 672px;
    background: var(--paper);
  }
  .sign__art {
    position: absolute;
    inset: 0;
    width: 1200px;
    height: 672px;
  }
  .brand-mark {
    fill: none;
    stroke: var(--ink);
    stroke-width: 9;
  }
  .brand-name {
    font-family: "Oswald", sans-serif;
    font-weight: 600;
    fill: var(--ink);
  }
  .headline-big {
    font-family: "Oswald", sans-serif;
    font-weight: 600;
    fill: var(--ink);
  }
  .headline-small {
    font-family: "Archivo", sans-serif;
    font-weight: 700;
    fill: var(--ink);
  }
</style>
</head>
<body>
<main class="sign">
  <svg class="sign__art" viewBox="0 0 1200 672" xmlns="http://www.w3.org/2000/svg">
    <g class="brand">
      <circle class="brand-mark" cx="284" cy="276" r="122"/>
      <text class="brand-name" x="94" y="468" font-size="62" textLength="384" lengthAdjust="spacingAndGlyphs">HARLOW</text>
      <text class="brand-name" x="121" y="510" font-size="28" textLength="330" lengthAdjust="spacingAndGlyphs">ORTHOPEDIC CLINIC</text>
    </g>

    <g class="headline">
      <text class="headline-small" x="656" y="196" font-size="36" textLength="68" lengthAdjust="spacingAndGlyphs">THE</text>
      <text class="headline-big" x="632" y="272" font-size="88" textLength="334" lengthAdjust="spacingAndGlyphs">GOOD LORD</text>

      <text class="headline-small" transform="translate(584 352) rotate(-90)" x="0" y="0" font-size="36" textLength="94" lengthAdjust="spacingAndGlyphs">DOES</text>
      <text class="headline-big" x="596" y="356" font-size="88" textLength="108" lengthAdjust="spacingAndGlyphs">ALL</text>
      <text class="headline-small" x="702" y="334" font-size="33" textLength="66" lengthAdjust="spacingAndGlyphs">THE</text>
      <text class="headline-big" x="780" y="356" font-size="88" textLength="322" lengthAdjust="spacingAndGlyphs">HEALING...</text>

      <text class="headline-big" x="554" y="460" font-size="94" textLength="82" lengthAdjust="spacingAndGlyphs">BUT</text>
      <text class="headline-small" x="670" y="438" font-size="33" textLength="56" lengthAdjust="spacingAndGlyphs">WE</text>
      <text class="headline-big" x="738" y="456" font-size="98" textLength="74" lengthAdjust="spacingAndGlyphs">DO</text>
      <text class="headline-small" x="834" y="410" font-size="37" textLength="250" lengthAdjust="spacingAndGlyphs">COLLECT THE</text>
      <text class="headline-big" x="852" y="502" font-size="108" textLength="224" lengthAdjust="spacingAndGlyphs">CO-PAY</text>
    </g>
  </svg>
</main>
</body>
</html>
```